New Consulting Firm News PowerPoint Template

We are a new consulting firm that specializes in Veltrix Unified Planning Suite implementations in need of a new PowerPoint template. We need at least the following layouts:
• Main Cover Slide
• Agenda / Table of Contents
• Title slide for each of the agenda items leading into actual content
• Title + Content with nice bullets in the content
• Title + Sub-Title + Content with nice bullets in the content
• Title + Two Columns of Content
• Title + Sub-Title + Two Columns of Content
• Title + Three Columns of Content
• Title + Sub-Title + Three Columns of Content
• Title + Two Rows and Two Columns of Content (4 boxes)
• Title + Sub-Title + Two Rows and Two Columns of Content (4 boxes)
• Title + Blank
• Nascar Slide (Client logos arranged somehow)
• Case Study Slide
• Various infographic slides than can be used and modified would be amazing as well
Our logo has been uploaded and you can find our website here:
https://brannowadvisory.com
We would like the main theme colors to blend with our logo, but also have a variety of colors in the theme that compliment the main theme colors. Once we have selected a PowerPoint design we expect to immediately have a Word design contest and the winning PowerPoint design will likely be a heavy influence on the Word design.

Target Market(s)

CFO, CAO, VP of Finance, Controllers

Industry/Entity Type

Consulting

Font styles to use
Serif
Sans Serif

Requirements
Must have
• • Main Cover Slide
• Title + Blank
• Case Study Slide
Nice to have
• • Various infographic slides than can be used and modified would be amazing as well

```html
<!DOCTYPE html>
<html lang="en">
<head>
<meta charset="utf-8">
<title>Brannow Advisory – Presentation Template</title>
<link href="https://fonts.googleapis.com/css2?family=Arimo:wght@400;700&display=swap" rel="stylesheet">
<style>
:root{
  --blue:#1f6fc5;
  --blue-soft:#3f8ae0;
  --navy:#2b3f8f;
  --deep:#1d2f6e;
  --grey:#6b7079;
  --ink:#1c1f24;
  --text:#555a62;
  --paper:#ffffff;
  --mist:#e8edf3;
  --page:#ffffff;
}
*{box-sizing:border-box;margin:0;padding:0}
html,body{width:1200px;height:3849px;overflow:hidden;background:var(--page);font-family:"Arimo",Arial,sans-serif;color:var(--ink)}
.canvas{position:relative;width:1200px;height:3849px}

/* showcase header */
.showcase{position:absolute;left:0;top:0;width:1200px;height:770px;background:linear-gradient(180deg,#eef1f5,#dfe4ea)}
.showcase-frame{position:absolute;left:70px;top:150px;width:562px;height:317px;transform:scale(1.42);transform-origin:0 0;box-shadow:0 10px 30px rgba(30,40,70,.25)}
.wordmark{position:absolute;left:930px;top:110px;text-align:center;width:190px}
.wordmark .sq{width:60px;height:60px;background:var(--navy);margin:0 auto 14px}
.wordmark .name{font-size:34px;font-weight:700;color:var(--navy);letter-spacing:2px}
.wordmark .tag{font-size:12px;font-weight:700;color:var(--navy);letter-spacing:4px;margin-top:4px}

/* slide base */
.slide{position:absolute;width:562px;height:317px;background:var(--paper);overflow:hidden;box-shadow:0 1px 4px rgba(0,0,0,.18)}
.L{left:28px}.R{left:610px}
.head{position:absolute;top:26px;left:0;right:0;text-align:center}
.head h2{font-size:21px;font-weight:700;color:var(--ink)}
.head .sub{font-size:10px;color:var(--grey);margin-top:2px}
.dots{display:flex;gap:4px;justify-content:center;margin-top:6px}
.dots i{width:6px;height:6px;border-radius:50%;background:var(--blue)}
.dots i:last-child{background:var(--grey)}
.head.light h2{color:#fff}.head.light .dots i{background:#fff}
.foot .mark{position:absolute;left:30px;bottom:9px;display:flex;align-items:center;gap:4px;font-size:7px;font-weight:700;color:var(--navy)}
.foot .mark b{width:12px;height:12px;background:var(--navy);display:block}
.foot .legal{position:absolute;right:50px;bottom:11px;font-size:5px;color:var(--grey)}
.foot .pg{position:absolute;right:22px;bottom:7px;width:14px;height:14px;border-radius:50%;background:var(--blue);color:#fff;font-size:7px;text-align:center;line-height:14px;font-weight:700}
.lorem{font-size:6px;line-height:1.35;color:var(--text)}
.pill{height:18px;border-radius:9px;color:#fff;font-size:9px;font-weight:700;line-height:18px;padding-left:14px}
.pill.blue{background:var(--blue)}.pill.grey{background:var(--grey)}.pill.navy{background:var(--navy)}
.art{position:absolute}

/* cover */
.cover-top{position:absolute;left:0;top:0;width:562px;height:94px;background:#fff}
.logo{position:absolute;left:48px;top:22px;display:flex;align-items:center;gap:6px;font-size:11px;font-weight:700;color:var(--navy);letter-spacing:1px}
.logo b{width:22px;height:22px;background:var(--navy);display:block}
.cover-hero{position:absolute;left:0;top:94px;width:562px;height:203px;background:linear-gradient(100deg,#c9d3e0,#eef2f7 60%,#dde4ee)}
.cover-band{position:absolute;left:0;bottom:0;width:562px;height:20px;background:var(--blue);color:#fff;font-size:5px;text-align:center;line-height:20px}
.cover-title{position:absolute;right:50px;top:130px;text-align:right;color:var(--blue);font-size:24px;font-weight:700;line-height:1.1}
.cover-lede{position:absolute;right:50px;top:190px;width:330px;text-align:center;font-size:7px;color:#39404a;line-height:1.3}
.cover-date{position:absolute;right:50px;top:255px;font-size:7px;color:var(--ink)}

/* toc */
.toc{position:absolute;top:95px;left:70px;right:40px;display:grid;grid-template-columns:1fr 1fr;row-gap:22px;column-gap:20px}
.toc-item{display:flex;gap:12px;align-items:flex-start}
.toc-item .n{font-size:18px;font-weight:700;color:var(--navy);width:14px}
.toc-item h4{font-size:11px;font-weight:700;color:var(--blue)}
.toc-item.alt h4{color:var(--grey);font-weight:400}

/* columns */
.cols{position:absolute;display:grid}
.col h4{font-size:10px;color:var(--blue);font-weight:700}
.col ul{list-style:none}
.bul{margin:4px 0 3px 14px;font-size:7px;line-height:1.3;color:var(--ink)}
.bul:before{content:"• ";font-weight:700}
.sbul{margin:0 0 8px 26px;font-size:5.5px;color:var(--text)}
.sbul:before{content:"• "}
.circ{width:46px;height:46px;border-radius:50%;margin:0 auto;display:flex;align-items:center;justify-content:center;border:3px solid #fff;box-shadow:0 0 0 1px #cfd6e0}
.pill-ico{display:flex;align-items:center;height:20px;border-radius:10px;color:#fff;font-size:9px;font-weight:700}
.pill-ico .ic{width:26px;height:26px;border-radius:50%;background:#fff;border:3px solid currentColor;margin-left:-3px;margin-right:10px;display:flex;align-items:center;justify-content:center}
.box{border:1px solid #d6dbe2;border-radius:10px;padding:16px 12px 8px;position:relative;text-align:center}
.box .tab{position:absolute;top:-7px;left:20px;height:14px;padding:0 14px;border-radius:3px;font-size:7px;font-weight:700;color:#fff;line-height:14px}
.client{font-size:11px;font-weight:700;text-align:center}
.contact{position:absolute;left:50px;top:110px;color:#fff}
.contact h4{font-size:12px;font-weight:700;margin:30px 0 6px}
.contact p{font-size:7px;line-height:1.4}
.contact .row{display:flex;align-items:center;gap:6px;font-size:6.5px;margin-top:6px}
</style>
</head>
<body>
<div class="canvas">

<section class="showcase">
  <div class="showcase-frame slide" style="left:70px;top:150px">
    <div class="cover-top"><div class="logo"><b></b>BRANNOW</div></div>
    <div class="cover-hero"></div>
    <div class="art" role="img" aria-label="Floating grey cubes over a faint network pattern" style="left:0;top:94px;width:240px;height:203px;background:linear-gradient(135deg,#b8c3d2,#dfe5ed)"></div>
    <svg class="art" width="562" height="317" style="left:0;top:0"><polygon points="520,0 562,0 562,150 520,110" fill="#1f6fc5"/><polygon points="490,30 520,10 520,110 490,90" fill="#5a93d6"/></svg>
    <div class="cover-title">Innovative EPM Solutions<br>for Finance and Beyond</div>
    <div class="cover-lede">Brannow Advisory provides decades of experience implementing Veltrix EPM products with unique and innovative solutions to challenging business process not only in Finance and Accounting, but across organizations.</div>
    <div class="cover-date">Monday, March 15, 2021</div>
    <div class="cover-band">Brannow Advisory, LLC © All Rights Reserved</div>
  </div>
  <div class="wordmark"><div class="sq"></div><div class="name">BRANNOW</div><div class="tag">ADVISORY</div></div>
</section>

<!-- 1 cover -->
<div class="slide L" style="top:790px">
  <div class="cover-top"><div class="logo"><b></b>BRANNOW</div></div>
  <div class="cover-hero"></div>
  <div class="art" role="img" aria-label="Floating grey cubes over a faint network pattern" style="left:0;top:94px;width:240px;height:203px;background:linear-gradient(135deg,#b8c3d2,#dfe5ed)"></div>
  <svg class="art" width="562" height="317" style="left:0;top:0"><polygon points="520,0 562,0 562,150 520,110" fill="#1f6fc5"/><polygon points="490,30 520,10 520,110 490,90" fill="#5a93d6"/></svg>
  <div class="cover-title">Innovative EPM Solutions<br>for Finance and Beyond</div>
  <div class="cover-lede">Brannow Advisory provides decades of experience implementing Veltrix EPM products with unique and innovative solutions to challenging business process not only in Finance and Accounting, but across organizations.</div>
  <div class="cover-date">Monday, March 15, 2021</div>
  <div class="cover-band">Brannow Advisory, LLC © All Rights Reserved</div>
</div>

<!-- 2 title -->
<div class="slide R" style="top:790px">
  <div class="cover-top"><div class="logo"><b></b>BRANNOW</div></div>
  <div class="cover-hero"></div>
  <div class="art" role="img" aria-label="Floating grey cubes on the right side" style="left:330px;top:94px;width:232px;height:203px;background:linear-gradient(225deg,#b8c3d2,#e6ebf2)"></div>
  <svg class="art" width="562" height="317" style="left:0;top:0"><polygon points="520,0 562,0 562,150 520,110" fill="#1f6fc5"/><polygon points="490,30 520,10 520,110 490,90" fill="#5a93d6"/></svg>
  <div style="position:absolute;left:48px;top:130px;color:var(--navy);font-size:24px;font-weight:700;line-height:1.1">Presentation Title<br>Goes Here!</div>
  <div style="position:absolute;left:48px;top:195px;font-size:13px;color:var(--ink);line-height:1.2">Subtitle of Presentation<br>Goes Here!</div>
  <div style="position:absolute;left:48px;top:255px;font-size:7px">Monday, March 15, 2021</div>
  <div class="cover-band">Brannow Advisory, LLC © All Rights Reserved</div>
</div>

<!-- 3 toc -->
<div class="slide L" style="top:1125px">
  <div class="head"><h2>Table of Contents</h2><div class="dots"><i></i><i></i><i></i></div></div>
  <div class="toc">
    <div class="toc-item"><span class="n">1</span><div><h4>Title Goes Here!</h4><p class="lorem">Lorem ipsum dolor sit amet, at laborum nibh duis mauris. Per ultrices lectus sed.</p></div></div>
    <div class="toc-item alt"><span class="n">2</span><div><h4>Title Goes Here!</h4><p class="lorem">Lorem ipsum dolor sit amet, at laborum nibh duis mauris. Per ultrices lectus sed.</p></div></div>
    <div class="toc-item"><span class="n">3</span><div><h4>Title Goes Here!</h4><p class="lorem">Lorem ipsum dolor sit amet, at laborum nibh duis mauris. Per ultrices lectus sed.</p></div></div>
    <div class="toc-item"><span class="n">4</span><div><h4>Title Goes Here!</h4><p class="lorem">Lorem ipsum dolor sit amet, at laborum nibh duis mauris. Per ultrices lectus sed.</p></div></div>
    <div class="toc-item alt"><span class="n">5</span><div><h4>Title Goes Here!</h4><p class="lorem">Lorem ipsum dolor sit amet, at laborum nibh duis mauris. Per ultrices lectus sed.</p></div></div>
    <div class="toc-item"><span class="n">6</span><div><h4>Title Goes Here!</h4><p class="lorem">Lorem ipsum dolor sit amet, at laborum nibh duis mauris. Per ultrices lectus sed.</p></div></div>
  </div>
  <div class="foot"><div class="mark"><b></b>BRANNOW</div><div class="legal">Brannow Advisory, LLC © All Rights Reserved</div><div class="pg">3</div></div>
</div>

<!-- 4 why -->
<div class="slide R" style="top:1125px">
  <div class="head"><h2>Why Choose Brannow?</h2><div class="dots"><i></i><i></i><i></i></div></div>
  <div style="position:absolute;left:38px;top:95px;width:320px;font-size:7.5px;line-height:1.3;color:var(--text)">
    <p><b style="color:var(--blue)">Brannow Advisory</b> was founded on the principles of innovation and teamwork. We innovate the products we implement through a combination of functional experience and technical expertise. When we find limitations in the products that we implement, we see this as an opportunity and a challenge to extend those products until we meet the needs of our clients. Through this innovation we have created various tools to accelerate our implementations.</p>
    <p style="margin-top:6px">Part of this innovation is how we at Brannow view our teams and projects. Whether a project is staffed by one consultant or ten consultants, we bring the full force of our team and our ability to support one another regardless of project assignments. You don't just get part of Brannow, you get the entire team.</p>
  </div>
  <div class="art" role="img" aria-label="Illustration of a team working around a meeting table, seen from above" style="left:380px;top:70px;width:170px;height:200px;border-radius:14px;background:linear-gradient(160deg,#e6e9ee,#c9ced6)"></div>
  <div class="foot"><div class="mark"><b></b>BRANNOW</div><div class="legal">Brannow Advisory, LLC © All Rights Reserved</div><div class="pg">4</div></div>
</div>

<!-- 5 section -->
<div class="slide L" style="top:1460px">
  <div class="art" role="img" aria-label="Office photo tinted deep blue" style="left:0;top:0;width:562px;height:125px;background:linear-gradient(120deg,#1d2f6e,#2e52a8)"></div>
  <div class="head light" style="top:26px"><h2 style="font-size:19px;line-height:1.15">Innovative Veltrix EPM Solutions to Drive<br>Organizational Change</h2><div class="dots"><i></i><i></i><i></i></div></div>
  <div class="cols" style="left:40px;right:40px;top:118px;grid-template-columns:repeat(3,1fr);gap:20px;text-align:center">
    <div><div class="circ" style="background:var(--blue)"><svg width="24" height="24" viewBox="0 0 24 24" fill="none" stroke="#fff" stroke-width="1.6"><circle cx="12" cy="6" r="3"/><circle cx="5" cy="17" r="3"/><circle cx="19" cy="17" r="3"/></svg></div><h4 style="font-size:10px;margin:6px 0 6px">Who We Are</h4><p class="lorem">Experienced EPM resources with innovative solutions and a diverse skillset to ensure that any project can be successfully executed.</p></div>
    <div><div class="circ" style="background:var(--grey)"><svg width="24" height="24" viewBox="0 0 24 24" fill="none" stroke="#fff" stroke-width="1.6"><circle cx="12" cy="12" r="9"/><circle cx="12" cy="12" r="5"/><circle cx="12" cy="12" r="1.5" fill="#fff"/></svg></div><h4 style="font-size:10px;margin:6px 0 6px">Our Mission</h4><p class="lorem">Provide clients with the highest quality EPM experience using a proven methodology that ensures client interaction and satisfaction.</p></div>
    <div><div class="circ" style="background:var(--navy)"><svg width="24" height="24" viewBox="0 0 24 24" fill="none" stroke="#fff" stroke-width="1.6"><path d="M8 14a6 6 0 1 1 8 0v3H8z"/><path d="M10 20h4"/><path d="M9.5 10.5l2 2 3.5-4"/></svg></div><h4 style="font-size:10px;margin:6px 0 6px">Our Vision</h4><p class="lorem">Empower clients to adopt excellent EPM applications while having a positive impact on the EPM community at large through the knowledge we share.</p></div>
  </div>
  <div class="foot"><div class="mark"><b></b>BRANNOW</div><div class="legal">Brannow Advisory, LLC © All Rights Reserved</div><div class="pg">5</div></div>
</div>

<!-- 6 team -->
<div class="slide R" style="top:1460px">
  <div class="art" role="img" aria-label="Office photo tinted deep blue" style="left:0;top:0;width:562px;height:125px;background:linear-gradient(120deg,#1d2f6e,#2e52a8)"></div>
  <div class="head light"><h2>Meet Our Team</h2><div class="dots"><i></i><i></i><i></i></div></div>
  <div class="cols" style="left:40px;right:40px;top:78px;grid-template-columns:repeat(4,1fr);gap:20px;text-align:center">
    <div><div role="img" aria-label="Portrait photo of Bryce Holden" style="height:115px;background:linear-gradient(180deg,#dfe3e8,#a9b0ba)"></div><h4 style="color:var(--blue);font-size:10px;margin-top:6px">Bryce Holden</h4><p style="font-size:6px">EPM Solution Architect</p><p class="lorem" style="margin-top:5px">Bryce is an EPM Solution Architect and partner at Brannow with over 20 years of experience in EPM and IT.</p></div>
    <div><div role="img" aria-label="Portrait photo of Valeria Grant" style="height:115px;background:linear-gradient(180deg,#dfe3e8,#a9b0ba)"></div><h4 style="color:var(--blue);font-size:10px;margin-top:6px">Valeria Grant</h4><p style="font-size:6px">EPM Solution Architect</p><p class="lorem" style="margin-top:5px">Valeria is an EPM Solution Architect and certified manager with 25 years in accounting and EPM.</p></div>
    <div><div role="img" aria-label="Portrait photo of Colin Sheard" style="height:115px;background:linear-gradient(180deg,#dfe3e8,#a9b0ba)"></div><h4 style="color:var(--blue);font-size:10px;margin-top:6px">Colin Sheard</h4><p style="font-size:6px">EPM Integration Architect</p><p class="lorem" style="margin-top:5px">Colin is an EPM Integration Architect and partner with over 15 years in EPM and data technology.</p></div>
    <div><div role="img" aria-label="Portrait photo of Cristian Vale" style="height:115px;background:linear-gradient(180deg,#dfe3e8,#a9b0ba)"></div><h4 style="color:var(--blue);font-size:10px;margin-top:6px">Cristian Vale</h4><p style="font-size:6px">EPM Senior Consultant</p><p class="lorem" style="margin-top:5px">Cristian is a Senior Consultant with over 15 years in EPM, accounting and finance.</p></div>
  </div>
  <div class="foot"><div class="mark"><b></b>BRANNOW</div><div class="legal">Brannow Advisory, LLC © All Rights Reserved</div><div class="pg">6</div></div>
</div>

<!-- 7 bullets two col -->
<div class="slide L" style="top:1795px">
  <div class="head"><h2>Bullets Slide Title Goes Here!</h2><div class="dots"><i></i><i></i><i></i></div></div>
  <div class="cols" style="left:50px;right:40px;top:82px;grid-template-columns:1fr 1fr;gap:30px">
    <div class="col"><div class="pill blue">Title Goes Here!</div>
      <h4 style="margin-top:10px">• Title Goes Here!</h4><div class="bul">Lorem ipsum dolor sit amet, at laborum nibh duis mauris. Per ultrices lectus sed metus tristique eu.</div><div class="sbul">Diam suspendisse ac ipsum maecenas fermentum, aliquet imperdiet.</div>
      <h4>• Title Goes Here!</h4><div class="bul">Lorem ipsum dolor sit amet, at laborum nibh duis mauris. Per ultrices lectus sed metus tristique eu.</div><div class="sbul">Diam suspendisse ac ipsum maecenas fermentum, aliquet imperdiet.</div></div>
    <div class="col"><div class="pill grey">Title Goes Here!</div>
      <h4 style="margin-top:10px">• Title Goes Here!</h4><div class="bul">Lorem ipsum dolor sit amet, at laborum nibh duis mauris. Per ultrices lectus sed metus tristique eu.</div><div class="sbul">Diam suspendisse ac ipsum maecenas fermentum, aliquet imperdiet.</div>
      <h4>• Title Goes Here!</h4><div class="bul">Lorem ipsum dolor sit amet, at laborum nibh duis mauris. Per ultrices lectus sed metus tristique eu.</div><div class="sbul">Diam suspendisse ac ipsum maecenas fermentum, aliquet imperdiet.</div></div>
  </div>
  <div class="foot"><div class="mark"><b></b>BRANNOW</div><div class="legal">Brannow Advisory, LLC © All Rights Reserved</div><div class="pg">7</div></div>
</div>

<!-- 8 bullets single -->
<div class="slide R" style="top:1795px">
  <div class="head"><h2>Bullets Slide Title Goes Here!</h2><div class="sub">Subtitle of Slide Goes Here</div><div class="dots"><i></i><i></i><i></i></div></div>
  <div class="col" style="position:absolute;left:55px;right:50px;top:88px">
    <h4>• Title Goes Here!</h4><div class="bul">Lorem ipsum dolor sit amet, at laborum nibh duis mauris. Per ultrices lectus sed metus tristique eu.</div><div class="sbul">Diam suspendisse ac ipsum maecenas fermentum, aliquet imperdiet.</div>
    <h4>• Title Goes Here!</h4><div class="bul">Lorem ipsum dolor sit amet, at laborum nibh duis mauris. Per ultrices lectus sed metus tristique eu.</div><div class="sbul">Diam suspendisse ac ipsum maecenas fermentum, aliquet imperdiet.</div>
    <h4>• Title Goes Here!</h4><div class="bul">Lorem ipsum dolor sit amet, at laborum nibh duis mauris. Per ultrices lectus sed metus tristique eu.</div><div class="sbul">Diam suspendisse ac ipsum maecenas fermentum, aliquet imperdiet.</div>
  </div>
  <div class="foot"><div class="mark"><b></b>BRANNOW</div><div class="legal">Brannow Advisory, LLC © All Rights Reserved</div><div class="pg">8</div></div>
</div>

<!-- 9 two columns -->
<div class="slide L" style="top:2130px">
  <div class="head"><h2>Two Columns of Content</h2><div class="dots"><i></i><i></i><i></i></div></div>
  <div class="cols" style="left:35px;right:32px;top:95px;grid-template-columns:1fr 1fr;gap:28px">
    <div><div class="pill-ico" style="background:var(--blue);color:var(--blue)"><span class="ic"><svg width="12" height="12" viewBox="0 0 24 24" fill="none" stroke="currentColor" stroke-width="2.4"><path d="M8 14a6 6 0 1 1 8 0v3H8z"/></svg></span><span style="color:#fff">Title Goes Here!</span></div><p class="lorem" style="margin:22px 20px 0 40px">Lorem ipsum dolor sit amet, at laborum nibh duis mauris. Per ultrices lectus sed metus tristique eu. Diam suspendisse ac ipsum maecenas fermentum, aliquet imperdiet et lobortis venenatis nascetur lacus. A ac, vivamus erat nullam. Eu adipiscing pulvinar eros. Mollis malesuada vel scelerisque, ligula quam non mauris neque eleifend etiam. Tincidunt duis velit lacus phasellus dui vitae, nec eu. Sit vivamus amet turpis risus, tellus ultrices, velit cillum mauris lorem aenean, mollis a mollis in facilisis.</p></div>
    <div><div class="pill-ico" style="background:var(--grey);color:var(--blue)"><span class="ic"><svg width="12" height="12" viewBox="0 0 24 24" fill="none" stroke="currentColor" stroke-width="2.4"><circle cx="12" cy="12" r="8"/><circle cx="12" cy="12" r="3"/></svg></span><span style="color:#fff">Title Goes Here!</span></div><p class="lorem" style="margin:22px 20px 0 40px">Lorem ipsum dolor sit amet, at laborum nibh duis mauris. Per ultrices lectus sed metus tristique eu. Diam suspendisse ac ipsum maecenas fermentum, aliquet imperdiet et lobortis venenatis nascetur lacus. A ac, vivamus erat nullam. Eu adipiscing pulvinar eros. Mollis malesuada vel scelerisque, ligula quam non mauris neque eleifend etiam. Tincidunt duis velit lacus phasellus dui vitae, nec eu. Sit vivamus amet turpis risus, tellus ultrices, velit cillum mauris lorem aenean, mollis a mollis in facilisis.</p></div>
  </div>
  <div class="foot"><div class="mark"><b></b>BRANNOW</div><div class="legal">Brannow Advisory, LLC © All Rights Reserved</div><div class="pg">9</div></div>
</div>

<!-- 10 two columns sub -->
<div class="slide R" style="top:2130px">
  <div class="head"><h2>Two Columns of Content</h2><div class="sub">Subtitle of Slide Goes Here</div><div class="dots"><i></i><i></i><i></i></div></div>
  <div class="cols" style="left:35px;right:32px;top:104px;grid-template-columns:1fr 1fr;gap:28px">
    <div><div class="pill-ico" style="background:var(--blue);color:var(--blue)"><span class="ic"><svg width="12" height="12" viewBox="0 0 24 24" fill="none" stroke="currentColor" stroke-width="2.4"><path d="M8 14a6 6 0 1 1 8 0v3H8z"/></svg></span><span style="color:#fff">Title Goes Here!</span></div><p class="lorem" style="margin:20px 20px 0 40px">Lorem ipsum dolor sit amet, at laborum nibh duis mauris. Per ultrices lectus sed metus tristique eu. Diam suspendisse ac ipsum maecenas fermentum, aliquet imperdiet et lobortis venenatis nascetur lacus. A ac, vivamus erat nullam. Eu adipiscing pulvinar eros. Mollis malesuada vel scelerisque, ligula quam non mauris neque eleifend etiam. Tincidunt duis velit lacus phasellus dui vitae, nec eu. Sit vivamus amet turpis risus, tellus ultrices, velit cillum mauris lorem aenean, mollis a mollis in facilisis.</p></div>
    <div><div class="pill-ico" style="background:var(--grey);color:var(--blue)"><span class="ic"><svg width="12" height="12" viewBox="0 0 24 24" fill="none" stroke="currentColor" stroke-width="2.4"><circle cx="12" cy="12" r="8"/><circle cx="12" cy="12" r="3"/></svg></span><span style="color:#fff">Title Goes Here!</span></div><p class="lorem" style="margin:20px 20px 0 40px">Lorem ipsum dolor sit amet, at laborum nibh duis mauris. Per ultrices lectus sed metus tristique eu. Diam suspendisse ac ipsum maecenas fermentum, aliquet imperdiet et lobortis venenatis nascetur lacus. A ac, vivamus erat nullam. Eu adipiscing pulvinar eros. Mollis malesuada vel scelerisque, ligula quam non mauris neque eleifend etiam. Tincidunt duis velit lacus phasellus dui vitae, nec eu. Sit vivamus amet turpis risus, tellus ultrices, velit cillum mauris lorem aenean, mollis a mollis in facilisis.</p></div>
  </div>
  <div class="foot"><div class="mark"><b></b>BRANNOW</div><div class="legal">Brannow Advisory, LLC © All Rights Reserved</div><div class="pg">10</div></div>
</div>

<!-- 11 three columns -->
<div class="slide L" style="top:2465px">
  <div class="head"><h2>Three Columns of Content</h2><div class="dots"><i></i><i></i><i></i></div></div>
  <div class="cols" style="left:30px;right:32px;top:98px;grid-template-columns:repeat(3,1fr);gap:10px">
    <div><div class="pill blue">Title Goes Here!</div><p class="lorem" style="margin:20px 12px 0 18px">Lorem ipsum dolor sit amet, at laborum nibh duis mauris. Per ultrices lectus sed metus tristique eu. Diam suspendisse ac ipsum maecenas fermentum, aliquet imperdiet et lobortis venenatis nascetur lacus. A ac, vivamus erat nullam. Eu adipiscing pulvinar eros. Mollis malesuada vel scelerisque, ligula quam non mauris neque eleifend etiam. Tincidunt duis velit lacus phasellus.</p></div>
    <div><div class="pill grey">Title Goes Here!</div><p class="lorem" style="margin:20px 12px 0 18px">Lorem ipsum dolor sit amet, at laborum nibh duis mauris. Per ultrices lectus sed metus tristique eu. Diam suspendisse ac ipsum maecenas fermentum, aliquet imperdiet et lobortis venenatis nascetur lacus. A ac, vivamus erat nullam. Eu adipiscing pulvinar eros. Mollis malesuada vel scelerisque, ligula quam non mauris neque eleifend etiam. Tincidunt duis velit lacus phasellus.</p></div>
    <div><div class="pill navy">Title Goes Here!</div><p class="lorem" style="margin:20px 12px 0 18px">Lorem ipsum dolor sit amet, at laborum nibh duis mauris. Per ultrices lectus sed metus tristique eu. Diam suspendisse ac ipsum maecenas fermentum, aliquet imperdiet et lobortis venenatis nascetur lacus. A ac, vivamus erat nullam. Eu adipiscing pulvinar eros. Mollis malesuada vel scelerisque, ligula quam non mauris neque eleifend etiam. Tincidunt duis velit lacus phasellus.</p></div>
  </div>
  <div class="foot"><div class="mark"><b></b>BRANNOW</div><div class="legal">Brannow Advisory, LLC © All Rights Reserved</div><div class="pg">11</div></div>
</div>

<!-- 12 three columns sub -->
<div class="slide R" style="top:2465px">
  <div class="head"><h2>Three Columns of Content</h2><div class="sub">Subtitle of Slide Goes Here</div><div class="dots"><i></i><i></i><i></i></div></div>
  <div class="cols" style="left:30px;right:32px;top:106px;grid-template-columns:repeat(3,1fr);gap:10px">
    <div><div class="pill blue">Title Goes Here!</div><p class="lorem" style="margin:18px 12px 0 18px">Lorem ipsum dolor sit amet, at laborum nibh duis mauris. Per ultrices lectus sed metus tristique eu. Diam suspendisse ac ipsum maecenas fermentum, aliquet imperdiet et lobortis venenatis nascetur lacus. A ac, vivamus erat nullam. Eu adipiscing pulvinar eros. Mollis malesuada vel scelerisque, ligula quam non mauris neque eleifend etiam. Tincidunt duis velit lacus phasellus.</p></div>
    <div><div class="pill grey">Title Goes Here!</div><p class="lorem" style="margin:18px 12px 0 18px">Lorem ipsum dolor sit amet, at laborum nibh duis mauris. Per ultrices lectus sed metus tristique eu. Diam suspendisse ac ipsum maecenas fermentum, aliquet imperdiet et lobortis venenatis nascetur lacus. A ac, vivamus erat nullam. Eu adipiscing pulvinar eros. Mollis malesuada vel scelerisque, ligula quam non mauris neque eleifend etiam. Tincidunt duis velit lacus phasellus.</p></div>
    <div><div class="pill navy">Title Goes Here!</div><p class="lorem" style="margin:18px 12px 0 18px">Lorem ipsum dolor sit amet, at laborum nibh duis mauris. Per ultrices lectus sed metus tristique eu. Diam suspendisse ac ipsum maecenas fermentum, aliquet imperdiet et lobortis venenatis nascetur lacus. A ac, vivamus erat nullam. Eu adipiscing pulvinar eros. Mollis malesuada vel scelerisque, ligula quam non mauris neque eleifend etiam. Tincidunt duis velit lacus phasellus.</p></div>
  </div>
  <div class="foot"><div class="mark"><b></b>BRANNOW</div><div class="legal">Brannow Advisory, LLC © All Rights Reserved</div><div class="pg">12</div></div>
</div>

<!-- 13 2x2 -->
<div class="slide L" style="top:2800px">
  <div class="head"><h2>Two Rows and Two Columns of Content</h2><div class="dots"><i></i><i></i><i></i></div></div>
  <div class="cols" style="left:85px;right:60px;top:92px;grid-template-columns:1fr 1fr;gap:22px 18px">
    <div class="box"><span class="tab" style="background:var(--blue)">Title Goes Here!</span><p class="lorem">Lorem ipsum dolor sit amet, at laborum nibh duis mauris. Per ultrices lectus sed metus tristique eu. Diam suspendisse ac ipsum maecenas fermentum, aliquet imperdiet et lobortis venenatis nascetur lacus.</p></div>
    <div class="box"><span class="tab" style="background:var(--grey)">Title Goes Here!</span><p class="lorem">Lorem ipsum dolor sit amet, at laborum nibh duis mauris. Per ultrices lectus sed metus tristique eu. Diam suspendisse ac ipsum maecenas fermentum, aliquet imperdiet et lobortis venenatis nascetur lacus.</p></div>
    <div class="box"><span class="tab" style="background:var(--grey)">Title Goes Here!</span><p class="lorem">Lorem ipsum dolor sit amet, at laborum nibh duis mauris. Per ultrices lectus sed metus tristique eu. Diam suspendisse ac ipsum maecenas fermentum, aliquet imperdiet et lobortis venenatis nascetur lacus.</p></div>
    <div class="box"><span class="tab" style="background:var(--blue)">Title Goes Here!</span><p class="lorem">Lorem ipsum dolor sit amet, at laborum nibh duis mauris. Per ultrices lectus sed metus tristique eu. Diam suspendisse ac ipsum maecenas fermentum, aliquet imperdiet et lobortis venenatis nascetur lacus.</p></div>
  </div>
  <div class="foot"><div class="mark"><b></b>BRANNOW</div><div class="legal">Brannow Advisory, LLC © All Rights Reserved</div><div class="pg">13</div></div>
</div>

<!-- 14 2x2 sub -->
<div class="slide R" style="top:2800px">
  <div class="head"><h2>Two Rows and Two Columns of Content</h2><div class="sub">Subtitle of Slide Goes Here</div><div class="dots"><i></i><i></i><i></i></div></div>
  <div class="cols" style="left:85px;right:60px;top:100px;grid-template-columns:1fr 1fr;gap:20px 18px">
    <div class="box"><span class="tab" style="background:var(--blue)">Title Goes Here!</span><p class="lorem">Lorem ipsum dolor sit amet, at laborum nibh duis mauris. Per ultrices lectus sed metus tristique eu. Diam suspendisse ac ipsum maecenas fermentum, aliquet imperdiet et lobortis venenatis nascetur lacus.</p></div>
    <div class="box"><span class="tab" style="background:var(--grey)">Title Goes Here!</span><p class="lorem">Lorem ipsum dolor sit amet, at laborum nibh duis mauris. Per ultrices lectus sed metus tristique eu. Diam suspendisse ac ipsum maecenas fermentum, aliquet imperdiet et lobortis venenatis nascetur lacus.</p></div>
    <div class="box"><span class="tab" style="background:var(--grey)">Title Goes Here!</span><p class="lorem">Lorem ipsum dolor sit amet, at laborum nibh duis mauris. Per ultrices lectus sed metus tristique eu. Diam suspendisse ac ipsum maecenas fermentum, aliquet imperdiet et lobortis venenatis nascetur lacus.</p></div>
    <div class="box"><span class="tab" style="background:var(--blue)">Title Goes Here!</span><p class="lorem">Lorem ipsum dolor sit amet, at laborum nibh duis mauris. Per ultrices lectus sed metus tristique eu. Diam suspendisse ac ipsum maecenas fermentum, aliquet imperdiet et lobortis venenatis nascetur lacus.</p></div>
  </div>
  <div class="foot"><div class="mark"><b></b>BRANNOW</div><div class="legal">Brannow Advisory, LLC © All Rights Reserved</div><div class="pg">14</div></div>
</div>

<!-- 15 blank -->
<div class="slide L" style="top:3135px">
  <div class="head"><h2>Blank Slide with Title</h2><div class="dots"><i></i><i></i><i></i></div></div>
  <div class="foot"><div class="mark"><b></b>BRANNOW</div><div class="legal">Brannow Advisory, LLC © All Rights Reserved</div><div class="pg">15</div></div>
</div>

<!-- 16 nascar -->
<div class="slide R" style="top:3135px">
  <div class="head"><h2>Nascar Slide</h2><div class="dots"><i></i><i></i><i></i></div></div>
  <div class="art" role="img" aria-label="Photo of a business handshake over a desk" style="left:0;top:85px;width:562px;height:90px;background:linear-gradient(90deg,#c7d2df,#8e9bad 55%,#d6dce4)"></div>
  <div class="cols" style="left:30px;right:30px;top:190px;grid-template-columns:repeat(5,1fr);gap:22px 10px">
    <div class="client" style="color:#c4161c">Kestrel Mart</div>
    <div class="client" style="color:#e8891b">Emberline</div>
    <div class="client" style="color:#5a5f66">Northvale</div>
    <div class="client" style="color:#2e8b3e">Quartzbase</div>
    <div class="client" style="color:#2b3f8f">Hollowware</div>
    <div class="client" style="color:#d1497a">Tenvio</div>
    <div class="client" style="color:#1f6fc5">Praxon</div>
    <div class="client" style="color:#b5227e">ShopCove</div>
    <div class="client" style="color:#1c1f24">Wavelist</div>
    <div class="client" style="color:#e05a1f">Hostpanel</div>
  </div>
  <div class="foot"><div class="mark"><b></b>BRANNOW</div><div class="legal">Brannow Advisory, LLC © All Rights Reserved</div><div class="pg">16</div></div>
</div>

<!-- 17 case study -->
<div class="slide L" style="top:3470px">
  <div class="art" role="img" aria-label="Photo of a desk with laptop and coffee tinted blue" style="left:0;top:0;width:562px;height:170px;background:linear-gradient(120deg,#2a4590,#4f7bc4)"></div>
  <div class="head light"><h2>Case Study Slide</h2><div class="dots"><i></i><i></i><i></i></div></div>
  <p style="position:absolute;left:40px;right:40px;top:80px;text-align:center;color:#fff;font-size:8px;line-height:1.35">Lorem ipsum dolor sit amet, at laborum nibh duis mauris. Per ultrices lectus sed metus tristique eu. Diam suspendisse ac ipsum maecenas fermentum, aliquet imperdiet et lobortis venenatis nascetur lacus. A ac, vivamus erat nullam.</p>
  <div class="cols" style="left:50px;right:50px;top:145px;grid-template-columns:repeat(3,1fr);gap:24px;text-align:center">
    <div><div class="circ" style="background:var(--blue)"><svg width="22" height="22" viewBox="0 0 24 24" fill="none" stroke="#fff" stroke-width="1.6"><path d="M8 14a6 6 0 1 1 8 0v3H8z"/><path d="M10 20h4"/></svg></div><h4 style="font-size:9px;margin:8px 0 4px">Title Goes Here!</h4><p class="lorem">Lorem ipsum dolor sit amet, at laborum nibh duis mauris. Per ultrices lectus sed metus tristique eu. Diam suspendisse ac ipsum maecenas fermentum.</p></div>
    <div><div class="circ" style="background:var(--grey)"><svg width="22" height="22" viewBox="0 0 24 24" fill="none" stroke="#fff" stroke-width="1.8"><circle cx="10" cy="10" r="6"/><path d="M15 15l5 5"/></svg></div><h4 style="font-size:9px;margin:8px 0 4px">Title Goes Here!</h4><p class="lorem">Lorem ipsum dolor sit amet, at laborum nibh duis mauris. Per ultrices lectus sed metus tristique eu. Diam suspendisse ac ipsum maecenas fermentum.</p></div>
    <div><div class="circ" style="background:var(--navy)"><svg width="22" height="22" viewBox="0 0 24 24" fill="none" stroke="#fff" stroke-width="1.6"><rect x="3" y="5" width="18" height="12"/><path d="M9 21h6M12 17v4M6 14l4-4 3 3 5-5"/></svg></div><h4 style="font-size:9px;margin:8px 0 4px">Title Goes Here!</h4><p class="lorem">Lorem ipsum dolor sit amet, at laborum nibh duis mauris. Per ultrices lectus sed metus tristique eu. Diam suspendisse ac ipsum maecenas fermentum.</p></div>
  </div>
  <div class="foot"><div class="mark"><b></b>BRANNOW</div><div class="legal">Brannow Advisory, LLC © All Rights Reserved</div><div class="pg">17</div></div>
</div>

<!-- 18 contact -->
<div class="slide R" style="top:3470px;background:linear-gradient(120deg,#233c8a,#2f63b8)">
  <svg class="art" width="562" height="317" style="left:0;top:0"><polygon points="470,60 562,10 562,230 470,280" fill="#3f8ae0" opacity=".55"/><polygon points="510,40 562,15 562,200 510,230" fill="#6fa8ec" opacity=".6"/></svg>
  <div class="contact">
    <div style="display:flex;align-items:center;gap:6px;font-size:11px;font-weight:700;letter-spacing:1px"><span style="width:20px;height:20px;background:#fff;display:block"></span>BRANNOW</div>
    <h4>Contact Us</h4>
    <p>2480 Ridgeview Drive, Suite 210,<br>Alder Falls, Texas 75901</p>
    <div class="row" style="margin-top:12px"><svg width="9" height="9" viewBox="0 0 24 24" fill="#fff"><path d="M6 2l4 4-2 3a12 12 0 0 0 7 7l3-2 4 4-3 4C10 22 2 14 2 5z"/></svg>(555) 318-2047</div>
    <div class="row"><svg width="9" height="9" viewBox="0 0 24 24" fill="none" stroke="#fff" stroke-width="2"><circle cx="12" cy="12" r="4"/><path d="M16 12v2a3 3 0 0 0 6 0v-2a10 10 0 1 0-4 8"/></svg>info@brannowadvisory.com</div>
    <div class="row"><svg width="9" height="9" viewBox="0 0 24 24" fill="none" stroke="#fff" stroke-width="2"><circle cx="12" cy="12" r="9"/><path d="M3 12h18M12 3c3 3 3 15 0 18M12 3c-3 3-3 15 0 18"/></svg>https://brannowadvisory.com</div>
  </div>
  <div class="cover-band" style="background:var(--blue)">Brannow Advisory, LLC © All Rights Reserved</div>
</div>

</div>
</body>
</html>
```